Design for a 4 screens iOS and Android app - "VelidMetra"

The app allows you to track your car gasoline refill ...
We need a design for the 4 screens of the app:
a) 1 form with 3 fields.
b) 1 simple list view
c) 1 summary view
d) 1 text page
2 "alerts" items are also to be designed.
No specific guidelines, nor logo or whatever.
It will be a free app distributed on iOS and Androïd.
We just want to make it looking nice & very usable for end users.
Target Market(s)
B2C app
Industry/Entity Type
Android

```html
<!DOCTYPE html>
<html lang="en">
<head>
<meta charset="utf-8">
<title>VelidMetra – app screens</title>
<link rel="stylesheet" href="https://fonts.googleapis.com/css2?family=Lato:ital,wght@0,400;0,700;0,900;1,700&display=swap">
<style>
  :root {
    --canvas: #6b6b6b;
    --screen-bg: #dedede;
    --tab-bg: #f3f3f3;
    --tab-divider: #d4d4d4;
    --tab-active: #4a4a4a;
    --tab-idle: #b4b4b4;
    --accent: #f28a00;
    --accent-light: #ffb81c;
    --accent-dark: #f07f00;
    --field-bg: #ffffff;
    --field-border: #cfcfcf;
    --placeholder: #b0b0b0;
    --ink: #1e1e1e;
    --muted: #444444;
    --error: #e3202a;
    --error-bg: #fde2e2;
    --success: #3aa51f;
    --success-dark: #2d8a16;
    --status-ink: #222222;
  }
  * { box-sizing: border-box; }
  html, body { margin: 0; padding: 0; }
  body {
    width: 1200px;
    height: 2350px;
    overflow: hidden;
    background: var(--canvas);
    font-family: "Lato", sans-serif;
    position: relative;
  }
  .screen {
    position: absolute;
    width: 400px;
    height: 710px;
    background: var(--screen-bg);
    overflow: hidden;
  }
  .screen--form { left: 139px; top: 259px; }
  .screen--error { left: 667px; top: 259px; }
  .screen--saved { left: 139px; top: 1371px; }
  .screen--about { left: 667px; top: 1371px; }

  .status-bar {
    position: absolute; left: 0; top: 0; width: 100%; height: 28px;
    background: #ffffff;
    display: flex; align-items: center; justify-content: space-between;
    padding: 0 10px; font-size: 11px; color: var(--status-ink);
    z-index: 3;
  }
  .status-bar .signal { display: flex; align-items: center; gap: 2px; }
  .status-bar .dot { width: 6px; height: 6px; border-radius: 50%; background: var(--status-ink); }
  .status-bar .dot--empty { background: none; border: 1px solid var(--status-ink); }
  .status-bar .carrier { margin-left: 4px; }
  .status-bar .battery { display: flex; align-items: center; gap: 5px; }
  .status-bar .battery-cell { width: 24px; height: 11px; border: 1px solid var(--status-ink); padding: 1px; position: relative; }
  .status-bar .battery-cell::before { content: ""; display: block; width: 100%; height: 100%; background: var(--status-ink); }

  .tab-bar {
    position: absolute; left: 0; top: 28px; width: 100%; height: 86px;
    background: var(--tab-bg);
    display: flex;
    border-bottom: 5px solid var(--accent);
  }
  .tab {
    flex: 1; display: flex; flex-direction: column; align-items: center; justify-content: center;
    gap: 4px; font-size: 13px; font-weight: 700; color: var(--tab-idle);
    border-left: 1px solid var(--tab-divider);
  }
  .tab:first-child { border-left: none; }
  .tab--active { color: var(--tab-active); }
  .tab svg { width: 34px; height: 28px; }
  .tab-pointer {
    position: absolute; left: 57px; top: 119px; width: 0; height: 0;
    border-left: 9px solid transparent; border-right: 9px solid transparent;
    border-top: 9px solid var(--accent);
  }

  .field {
    position: absolute; left: 20px; width: 360px; height: 74px;
    background: var(--field-bg); border: 1px solid var(--field-border); border-radius: 16px;
    display: flex; align-items: center; justify-content: space-between;
    padding: 0 18px 0 20px; font-size: 27px; color: var(--ink);
  }
  .field--placeholder { color: var(--placeholder); font-size: 26px; }
  .field--error { background: var(--error-bg); border: 2px solid var(--error); }
  .field .field-end { display: flex; align-items: center; gap: 6px; }
  .field .error-note { font-size: 15px; font-style: italic; font-weight: 700; color: var(--error); }
  .field svg { width: 28px; height: 30px; }
  .field-odometer { top: 205px; }
  .field-litres { top: 291px; }
  .field-price { top: 379px; }

  .save-button {
    position: absolute; left: 20px; top: 472px; width: 360px; height: 75px;
    border-radius: 38px;
    background: linear-gradient(180deg, var(--accent-light) 0%, var(--accent) 60%, var(--accent-dark) 100%);
    display: flex; align-items: center; justify-content: center; gap: 14px;
    color: #ffffff; font-size: 27px; font-weight: 900;
    box-shadow: 0 2px 2px rgba(0,0,0,0.15);
  }
  .save-button svg { width: 34px; height: 32px; }
  .about-link {
    position: absolute; right: 20px; top: 562px;
    font-size: 16px; font-weight: 700; font-style: italic; color: var(--muted);
    text-decoration: underline;
  }

  .overlay {
    position: absolute; left: 0; top: 28px; right: 0; bottom: 0;
    background: rgba(40,40,40,0.62); z-index: 2;
  }
  .alert {
    position: absolute; left: 20px; top: 263px; width: 360px; height: 187px;
    border-radius: 10px; z-index: 4;
    background: linear-gradient(180deg, #ffffff 0%, #e2e2e2 100%);
    border: 1px solid #bdbdbd;
    display: flex; flex-direction: column; align-items: center; padding-top: 30px;
  }
  .alert-title { font-size: 19px; font-weight: 900; color: var(--success); margin: 0; }
  .alert svg { width: 72px; height: 62px; margin-top: 10px; }
  .alert-action { margin-top: 8px; font-size: 16px; font-weight: 700; font-style: italic; color: var(--ink); text-decoration: underline; }

  .page { position: absolute; left: 20px; top: 170px; width: 362px; }
  .page-title { margin: 0 0 10px; font-size: 26px; font-weight: 900; color: var(--accent); }
  .page p { margin: 0 0 22px; font-size: 16.5px; line-height: 25px; color: var(--ink); }
  .close-button {
    position: absolute; left: 20px; top: 583px; width: 360px; height: 54px;
    border-radius: 27px; border: 1px solid #c4c4c4;
    background: linear-gradient(180deg, #ffffff 0%, #dcdcdc 100%);
    display: flex; align-items: center; justify-content: center;
    font-size: 19px; font-weight: 900; color: #8a8a8a;
  }
</style>
</head>
<body>

<svg width="0" height="0" style="position:absolute">
  <defs>
    <symbol id="icon-add" viewBox="0 0 34 28"><path d="M1 4h11l3 3h18v20H1z" fill="currentColor"/><path d="M17 11v11M11.5 16.5h11" stroke="#fff" stroke-width="3"/></symbol>
    <symbol id="icon-list" viewBox="0 0 34 28"><g fill="currentColor"><rect x="2" y="3" width="5" height="5"/><rect x="10" y="3" width="22" height="5"/><rect x="2" y="11.5" width="5" height="5"/><rect x="10" y="11.5" width="22" height="5"/><rect x="2" y="20" width="5" height="5"/><rect x="10" y="20" width="22" height="5"/></g></symbol>
    <symbol id="icon-chart" viewBox="0 0 34 28"><path d="M3 2v24h29" stroke="currentColor" stroke-width="2.5" fill="none"/><path d="M6 24V8l5 4 5-6 5 9 4-3 5 5v7z" fill="currentColor"/></symbol>
    <symbol id="icon-pin" viewBox="0 0 28 30"><path d="M14 2a10 10 0 0 0-10 10c0 7 10 17 10 17s10-10 10-17A10 10 0 0 0 14 2z" fill="#c4c4c4"/><circle cx="14" cy="12" r="4" fill="#fff"/></symbol>
    <symbol id="icon-drop" viewBox="0 0 28 30"><path d="M14 2C10 9 5 14 5 19a9 9 0 0 0 18 0c0-5-5-10-9-17z" fill="currentColor"/><path d="M10 19a4 4 0 0 0 4 4" stroke="#fff" stroke-width="2" fill="none"/></symbol>
    <symbol id="icon-euro" viewBox="0 0 28 30"><path d="M22 6a10 10 0 1 0 0 18" stroke="#c4c4c4" stroke-width="4" fill="none"/><path d="M4 12h13M4 18h13" stroke="#c4c4c4" stroke-width="3"/></symbol>
    <symbol id="icon-save" viewBox="0 0 34 32"><rect x="1" y="6" width="24" height="24" fill="#fff"/><path d="M6 17l6 6L31 3" stroke="#f5a000" stroke-width="5" fill="none"/><path d="M6 17l6 6L31 3" stroke="#fff" stroke-width="2.5" fill="none" transform="translate(0,-1)"/></symbol>
  </defs>
</svg>

<!-- Screen: add entry form -->
<section class="screen screen--form">
  <div class="status-bar"><span class="signal"><i class="dot"></i><i class="dot"></i><i class="dot"></i><i class="dot"></i><i class="dot dot--empty"></i><span class="carrier">Carrier</span></span><span>5:30PM</span><span class="battery">100% <i class="battery-cell"></i></span></div>
  <nav class="tab-bar">
    <div class="tab tab--active"><svg><use href="#icon-add"/></svg>ADD</div>
    <div class="tab"><svg><use href="#icon-list"/></svg>LIST</div>
    <div class="tab"><svg><use href="#icon-chart"/></svg>CHART</div>
  </nav>
  <i class="tab-pointer"></i>
  <div class="field field-odometer">128500<svg><use href="#icon-pin"/></svg></div>
  <div class="field field-litres field--placeholder">LITRES<svg style="color:#c4c4c4"><use href="#icon-drop"/></svg></div>
  <div class="field field-price field--placeholder">PRICE<svg><use href="#icon-euro"/></svg></div>
  <div class="save-button"><svg><use href="#icon-save"/></svg>SAVE</div>
  <span class="about-link">About Us »</span>
</section>

<!-- Screen: validation error -->
<section class="screen screen--error">
  <div class="status-bar"><span class="signal"><i class="dot"></i><i class="dot"></i><i class="dot"></i><i class="dot"></i><i class="dot dot--empty"></i><span class="carrier">Carrier</span></span><span>5:30PM</span><span class="battery">100% <i class="battery-cell"></i></span></div>
  <nav class="tab-bar">
    <div class="tab tab--active"><svg><use href="#icon-add"/></svg>ADD</div>
    <div class="tab"><svg><use href="#icon-list"/></svg>LIST</div>
    <div class="tab"><svg><use href="#icon-chart"/></svg>CHART</div>
  </nav>
  <i class="tab-pointer"></i>
  <div class="field field-odometer">128500<svg><use href="#icon-pin"/></svg></div>
  <div class="field field-litres field--error">bbb<span class="field-end"><span class="error-note">Enter numbers</span><svg style="color:var(--error)"><use href="#icon-drop"/></svg></span></div>
  <div class="field field-price field--placeholder">PRICE<svg><use href="#icon-euro"/></svg></div>
  <div class="save-button"><svg><use href="#icon-save"/></svg>SAVE</div>
  <span class="about-link">About Us »</span>
</section>

<!-- Screen: saved alert -->
<section class="screen screen--saved">
  <div class="status-bar"><span class="signal"><i class="dot"></i><i class="dot"></i><i class="dot"></i><i class="dot"></i><i class="dot dot--empty"></i><span class="carrier">Carrier</span></span><span>5:30PM</span><span class="battery">100% <i class="battery-cell"></i></span></div>
  <nav class="tab-bar">
    <div class="tab tab--active"><svg><use href="#icon-add"/></svg>ADD</div>
    <div class="tab"><svg><use href="#icon-list"/></svg>LIST</div>
    <div class="tab"><svg><use href="#icon-chart"/></svg>CHART</div>
  </nav>
  <i class="tab-pointer"></i>
  <div class="field field-odometer">128500<svg><use href="#icon-pin"/></svg></div>
  <div class="save-button"><svg><use href="#icon-save"/></svg>SAVE</div>
  <span class="about-link">About Us »</span>
  <div class="overlay"></div>
  <div class="alert">
    <h2 class="alert-title">DATA SAVED</h2>
    <svg viewBox="0 0 72 62"><rect x="8" y="4" width="56" height="54" rx="3" fill="var(--success)"/><rect x="8" y="31" width="56" height="27" rx="3" fill="var(--success-dark)"/><path d="M20 31l11 11 22-24" stroke="#fff" stroke-width="8" fill="none"/></svg>
    <span class="alert-action">Okay »</span>
  </div>
</section>

<!-- Screen: text page -->
<section class="screen screen--about">
  <div class="status-bar"><span class="signal"><i class="dot"></i><i class="dot"></i><i class="dot"></i><i class="dot"></i><i class="dot dot--empty"></i><span class="carrier">Carrier</span></span><span>5:30PM</span><span class="battery">100% <i class="battery-cell"></i></span></div>
  <nav class="tab-bar">
    <div class="tab"><svg><use href="#icon-add"/></svg>ADD</div>
    <div class="tab"><svg><use href="#icon-list"/></svg>LIST</div>
    <div class="tab"><svg><use href="#icon-chart"/></svg>CHART</div>
  </nav>
  <article class="page">
    <h1 class="page-title">TITLE</h1>
    <p>Lorem ipsum dolor sit amet, consectetur adipis elit. Vivamus dignissim tellus sapien, at element justo egestas et. Maecenas tortor sem, pulvinar sit amet efficitur id, accumsan sit amet mi. Duis a efficitur augue, vel pellentesque est. Mauris id nisl nec neque elementum posuere non nam sed sapien in dolor ultrices eleifen quis eget lectus. Praesent vel sem non tortor lacinia.</p>
    <p>Quisque in lobortis velit aliqu. Donec mollis finibus scelerisque. Donec lobortis plact leo a fringilla curabitur gravida fermentum. neque vel rhoncus. Aenean ullamcorper elit enim, eget fermentum massa dignissim nec fusce sem.</p>
  </article>
  <div class="close-button">CLOSE</div>
</section>

</body>
</html>
```